Full service meeting planning company needs new business cards

Bright Harbor is a full service meeting planning company that specializes in on-line conference registration web development and event communications. We combine citywide hotel management, mobile applications, eblast reminders, confirmation letters, and customized reporting to create a seamless registration process. We also manage group motor coach transportation, food and beverages, entertainment, stage and lighting for group of 10 to 4000.

Target Market(s)

Corporations and associations

Industry/Entity Type

Event Planning

Contact Information for Business Card

standard size 3.5" wide and 2" tall

Font styles to use
Serif
Sans Serif

Colors
f37122
f78f20
333333
5c5c5c
9d9d9d
f68d4d

Requirements
Must have
• {name}
• Bright Harbor
• P.O. Box 7384, Grand Rapids, M I 49577
• www.brightharborplan.com
• {email}
• {phone}
• {mobile phone}
Nice to have
• Our colors are black, grey and orange as an accent color
Should not have
• I am not happy with our website layout anymore either. It feels dark and old but it does explain who we are pretty well if you'd like to review; www.brightharborplan.com

```html
<!DOCTYPE html>
<html lang="en">
<head>
<meta charset="utf-8">
<title>Bright Harbor — Business Cards</title>
<link href="https://fonts.googleapis.com/css2?family=Signika:wght@300;400;600&display=swap" rel="stylesheet">
<style>
  :root {
    --canvas: #e9e7e4;
    --card-white: #fbfbfa;
    --brand-orange: #f47439;
    --ink-white: #ffffff;
    --shadow: rgba(51, 51, 51, 0.18);
  }
  * { box-sizing: border-box; margin: 0; padding: 0; }
  html, body {
    width: 1200px;
    height: 982px;
    overflow: hidden;
    background: var(--canvas);
    font-family: "Signika", "Helvetica Neue", Arial, sans-serif;
  }
  .canvas {
    position: relative;
    width: 1200px;
    height: 982px;
  }
  .card {
    position: absolute;
    left: 250px;
    width: 700px;
    height: 400px;
    box-shadow: 0 10px 26px var(--shadow);
  }
  .card--front {
    top: 71px;
    background: var(--card-white);
    display: flex;
    flex-direction: column;
    align-items: center;
    justify-content: center;
    gap: 18px;
  }
  .card--back {
    top: 511px;
    background: var(--brand-orange);
    color: var(--ink-white);
  }
  .brand-mark {
    width: 96px;
    height: 96px;
    display: block;
  }
  .brand-name {
    font-weight: 400;
    font-size: 17px;
    letter-spacing: 0.22em;
    text-transform: uppercase;
    color: var(--brand-orange);
  }
  .back-brand {
    position: absolute;
    top: 44px;
    left: 56px;
    display: flex;
    align-items: center;
    gap: 10px;
  }
  .back-brand__dot {
    width: 30px;
    height: 30px;
    display: block;
  }
  .back-brand__name {
    font-weight: 400;
    font-size: 13px;
    letter-spacing: 0.18em;
    text-transform: uppercase;
    color: var(--ink-white);
  }
  .contact {
    position: absolute;
    top: 108px;
    left: 56px;
    font-weight: 300;
    font-size: 19px;
    line-height: 1.3;
  }
  .contact__name {
    font-weight: 600;
    font-size: 27px;
    letter-spacing: 0.01em;
  }
  .contact__title { margin-bottom: 4px; }
  .contact__sep {
    display: block;
    width: 4px;
    height: 4px;
    border-radius: 50%;
    background: var(--ink-white);
    margin: 6px 0 6px 4px;
  }
  .contact__label {
    display: inline-block;
    width: 26px;
  }
  .website {
    position: absolute;
    left: 56px;
    bottom: 30px;
    font-weight: 300;
    font-size: 13px;
    letter-spacing: 0.04em;
  }
</style>
</head>
<body>
<main class="canvas">
  <section class="card card--front" aria-label="Card front">
    <svg class="brand-mark" viewBox="0 0 96 96" aria-hidden="true">
      <circle cx="48" cy="48" r="44" fill="none" stroke="var(--brand-orange)" stroke-width="3"/>
    </svg>
    <p class="brand-name">Bright Harbor</p>
  </section>

  <section class="card card--back" aria-label="Card back">
    <div class="back-brand">
      <svg class="back-brand__dot" viewBox="0 0 30 30" aria-hidden="true">
        <circle cx="15" cy="15" r="14" fill="var(--ink-white)"/>
      </svg>
      <span class="back-brand__name">Bright Harbor</span>
    </div>

    <div class="contact">
      <p class="contact__name">Dana Whitfield</p>
      <p class="contact__title">CMP Sr. Project Manager</p>
      <p><span class="contact__label">P</span>616 555 0142</p>
      <p><span class="contact__label">F</span>616 555 0187</p>
      <span class="contact__sep"></span>
      <p>info@brightharborplan.com</p>
      <span class="contact__sep"></span>
      <p>P.O. Box 7384</p>
      <p>Grand Rapids, MI 49577</p>
    </div>

    <p class="website">www.brightharborplan.com</p>
  </section>
</main>
</body>
</html>
```